Business Card Design Project

Velvet Harbor is a Boutique Clothing. On the business cards I would like to have this included
Website: www.velvetharbor-example.com
Email: shop@velvetharbor-example.com
Owner: Mira Sol & Tor Dell

Industry/Entity Type

Business

Contact Information for Business Card

I wanted something simple and elegant. I have attach business logo.

```html
<!DOCTYPE html>
<html lang="en">
<head>
<meta charset="utf-8">
<title>Velvet Harbor — Business Card</title>
<link href="https://fonts.googleapis.com/css2?family=Lato:wght@400&family=Open+Sans:wght@400&display=swap" rel="stylesheet">
<style>
  :root {
    --page: #ece9e5;
    --card: #ffffff;
    --ink: #1e1e1e;
    --ink-soft: #3a3a3a;
    --ghost: #e6e6e6;
    --shadow: rgba(0, 0, 0, 0.12);
  }
  html, body {
    margin: 0;
    width: 1200px;
    height: 1200px;
    overflow: hidden;
    background: var(--page);
  }
  .canvas {
    width: 1200px;
    height: 1200px;
    display: flex;
    flex-direction: column;
    align-items: center;
    justify-content: center;
    gap: 60px;
  }
  .card {
    position: relative;
    width: 860px;
    height: 491px;
    background: var(--card);
    box-shadow: 0 6px 22px var(--shadow);
    overflow: hidden;
  }
  .brand {
    position: absolute;
    display: flex;
    flex-direction: column;
    align-items: center;
    font-family: "Lato", sans-serif;
    font-weight: 400;
    color: var(--ink);
  }
  .brand__ring {
    width: 16px;
    height: 16px;
    border: 2px solid currentColor;
    border-radius: 50%;
    margin-bottom: 22px;
  }
  .brand__name {
    font-size: 44px;
    letter-spacing: 0.32em;
    text-transform: uppercase;
    white-space: nowrap;
    margin-right: -0.32em;
  }
  .brand__tag {
    font-size: 15px;
    letter-spacing: 0.5em;
    text-transform: uppercase;
    margin-top: 14px;
    margin-right: -0.5em;
  }
  .card--front .brand {
    left: 50%;
    top: 50%;
    transform: translate(-50%, -50%);
  }
  .card--back .brand--main {
    left: 40px;
    top: 175px;
  }
  .card--back .brand--main .brand__name { font-size: 34px; }
  .card--back .brand--ghost {
    right: -60px;
    top: 30px;
    color: var(--ghost);
  }
  .card--back .brand--ghost .brand__name { font-size: 40px; }
  .owners {
    position: absolute;
    right: 56px;
    top: 150px;
    text-align: left;
    font-family: "Open Sans", sans-serif;
    color: var(--ink);
  }
  .owners__names {
    font-size: 26px;
    margin: 0;
  }
  .owners__role {
    font-size: 15px;
    margin: 2px 0 0;
    color: var(--ink-soft);
  }
  .contact {
    position: absolute;
    right: 56px;
    bottom: 56px;
    margin: 0;
    padding: 0;
    list-style: none;
    font-family: "Open Sans", sans-serif;
    font-size: 16px;
    color: var(--ink);
  }
  .contact__item {
    display: flex;
    align-items: center;
    gap: 10px;
    line-height: 28px;
  }
  .contact__icon {
    width: 16px;
    height: 16px;
    flex: none;
  }
</style>
</head>
<body>
<main class="canvas">
  <section class="card card--front" aria-label="Card front">
    <div class="brand">
      <span class="brand__ring"></span>
      <span class="brand__name">Velvet Harbor</span>
      <span class="brand__tag">Boutique</span>
    </div>
  </section>

  <section class="card card--back" aria-label="Card back">
    <div class="brand brand--ghost" aria-hidden="true">
      <span class="brand__name">Velvet Harbor</span>
    </div>
    <div class="brand brand--main">
      <span class="brand__ring"></span>
      <span class="brand__name">Velvet Harbor</span>
      <span class="brand__tag">Boutique</span>
    </div>

    <div class="owners">
      <p class="owners__names">Mira Sol &amp; Tor Dell</p>
      <p class="owners__role">Owner</p>
    </div>

    <ul class="contact">
      <li class="contact__item">
        <svg class="contact__icon" viewBox="0 0 16 16" aria-hidden="true"><path d="M4 1.5l2.2 3-1.3 1.5c.9 2 2.3 3.4 4.3 4.3l1.5-1.3 3 2.2-1.2 2.6C7.6 13.6 2.4 8.4 1.6 3.7z" fill="currentColor"/></svg>
        +1 555 010 2040
      </li>
      <li class="contact__item">
        <svg class="contact__icon" viewBox="0 0 16 16" aria-hidden="true"><rect x="1" y="3" width="14" height="10" fill="currentColor"/><path d="M1.5 3.5L8 9l6.5-5.5" stroke="#fff" stroke-width="1.2" fill="none"/></svg>
        shop@velvetharbor-example.com
      </li>
      <li class="contact__item">
        <svg class="contact__icon" viewBox="0 0 16 16" aria-hidden="true"><circle cx="8" cy="8" r="7" fill="currentColor"/><path d="M1 8h14M8 1c-2.5 2.5-2.5 11.5 0 14M8 1c2.5 2.5 2.5 11.5 0 14" stroke="#fff" stroke-width="1" fill="none"/></svg>
        www.velvetharbor-example.com
      </li>
    </ul>
  </section>
</main>
</body>
</html>
```